BRIGHTWAVE DENTAL *

please see attached.

Target Market(s)

Adults 18-60

Contact Information for Business Card

Website: brightwavedentalqz.com
Phone number 555 304 7726 email: brightwavedentalqz@mailvex.com
Address:417 S. Kellim rd
Suite#24, TX70000
Dr. Elias Varno, DDS

Font styles to use
Sans Serif

Requirements
Must have
• Logo, phone number website, doctor,
• 's name

```html
<!DOCTYPE html>
<html lang="en">
<head>
<meta charset="utf-8">
<title>Brightwave Dental – Business Card</title>
<link href="https://fonts.googleapis.com/css2?family=Lato:wght@300;400;700&display=swap" rel="stylesheet">
<style>
  :root {
    --backdrop: #5b5b5b;
    --card-dark: #1e1e1e;
    --card-light: #ffffff;
    --teal: #1a7f96;
    --ink: #3b3b3b;
    --ink-soft: #555555;
    --edge-grey: #4a4545;
  }
  * { margin: 0; padding: 0; box-sizing: border-box; }
  html, body { width: 1200px; height: 895px; overflow: hidden; }
  body {
    background: var(--backdrop);
    font-family: 'Lato', sans-serif;
    position: relative;
  }
  .card {
    position: absolute;
    left: 320px;
    width: 560px;
    height: 320px;
    border-radius: 26px;
    overflow: hidden;
    box-shadow: 0 10px 24px rgba(0,0,0,0.35);
  }
  .card--back { top: 100px; background: var(--card-dark); }
  .card--front { top: 470px; background: var(--card-light); }

  .card--back .edge-band {
    position: absolute; left: 0; right: 0; bottom: 0; height: 7px;
    background: var(--teal);
  }

  .brand {
    position: absolute;
    display: flex;
    align-items: center;
    gap: 14px;
  }
  .brand__mark { border-radius: 50%; flex-shrink: 0; }
  .brand__name {
    font-weight: 300;
    text-transform: uppercase;
    letter-spacing: 3px;
    white-space: nowrap;
  }
  .card--back .brand { left: 50%; top: 50%; transform: translate(-50%, -50%); }
  .card--back .brand__mark { width: 64px; height: 64px; border: 2px solid #ffffff; }
  .card--back .brand__name { color: #ffffff; font-size: 32px; }

  .card--front .brand { left: 26px; top: 34px; }
  .card--front .brand__mark { width: 54px; height: 54px; border: 2px solid var(--ink); }
  .card--front .brand__name { color: var(--ink); font-size: 26px; }

  .doctor { position: absolute; left: 120px; top: 138px; }
  .doctor__name {
    color: var(--teal);
    font-size: 28px;
    font-weight: 400;
    letter-spacing: 1px;
    text-transform: uppercase;
    white-space: nowrap;
  }
  .doctor__title {
    color: var(--ink-soft);
    font-size: 14px;
    letter-spacing: 1px;
    margin-top: 2px;
  }

  .contact { position: absolute; left: 120px; top: 220px; list-style: none; }
  .contact__item {
    display: flex; align-items: center; gap: 10px;
    color: var(--ink);
    font-size: 14px;
    line-height: 22px;
    white-space: nowrap;
  }
  .contact__item svg { width: 13px; height: 13px; flex-shrink: 0; }

  .address {
    position: absolute; right: 32px; top: 210px;
    color: var(--ink);
    font-size: 14px;
    font-style: normal;
    line-height: 20px;
    white-space: nowrap;
  }

  .footer-band {
    position: absolute; left: 0; right: 0; bottom: 0; height: 8px;
    display: flex;
  }
  .footer-band__dark { background: var(--edge-grey); }
  .footer-band__teal { background: var(--teal); }
</style>
</head>
<body>

  <section class="card card--back" aria-label="Card back">
    <div class="brand">
      <span class="brand__mark"></span>
      <span class="brand__name">Brightwave Dental</span>
    </div>
    <div class="edge-band"></div>
  </section>

  <section class="card card--front" aria-label="Card front">
    <div class="brand">
      <span class="brand__mark"></span>
      <span class="brand__name">Brightwave Dental</span>
    </div>

    <div class="doctor">
      <h1 class="doctor__name">Dr. Elias Varno</h1>
      <p class="doctor__title">DDS</p>
    </div>

    <ul class="contact">
      <li class="contact__item">
        <svg viewBox="0 0 16 16" fill="none" stroke="#1a7f96" stroke-width="1.5"><path d="M3 2h3l1.5 3.5-2 1.2a8 8 0 0 0 3.8 3.8l1.2-2L14 10v3a1 1 0 0 1-1 1A11 11 0 0 1 2 3a1 1 0 0 1 1-1z"/></svg>
        555 304 7726
      </li>
      <li class="contact__item">
        <svg viewBox="0 0 16 16" fill="none" stroke="#1a7f96" stroke-width="1.5"><rect x="1.5" y="3.5" width="13" height="9"/><path d="M1.5 3.5 8 9l6.5-5.5"/></svg>
        brightwavedentalqz@mailvex.com
      </li>
      <li class="contact__item">
        <svg viewBox="0 0 16 16" fill="none" stroke="#1a7f96" stroke-width="1.3"><circle cx="8" cy="8" r="6.5"/><ellipse cx="8" cy="8" rx="3" ry="6.5"/><path d="M1.5 8h13M3 4.5h10M3 11.5h10"/></svg>
        www.brightwavedentalqz.com
      </li>
    </ul>

    <address class="address">
      417 S. Kellim rd<br>
      Suite#24, TX70000
    </address>

    <div class="footer-band">
      <span class="footer-band__dark" style="width:120px"></span>
      <span class="footer-band__teal" style="width:280px"></span>
      <span class="footer-band__dark" style="flex:1"></span>
    </div>
  </section>

</body>
</html>
```